Bamboo Straw 4 Pack Cardboard Packaging

We would like a design with our logo and other bits of information for our 4 packs which will be in square cardboard packaging. We are all about the natural aspect of bamboo straws and saving our environment. Logos are attached as well as packaging option. The EXAMPLE there is not to be copied but used as inspiration. On the back of the package we will write our story.
Can use some of the facts below:
Bamboo is one most sustainable plants in the world! It can grow up to 1m in just 24 hours.
Bamboo is naturally anti- bacterial, anti fungal and odour resistant fibre
To grow Bamboo does not require fertiliser or any other harmful pesticides
Bamboo is a viable rep[lacement for wood. A Large tree can take over 35 years to mature, bamboo can take just 3, a single clump of bamboo can produce up to 15 kilometres of usable pole in its lifetime. It can out yield pine wood 6 to 1 in biomass production
It is the only plant left in the race to matching human consumption and deforestation one of its greatest qualities is after harvest its ability to renew growth is second to none
Bamboo straws are reusable and with care can last up to a year. They have anti bacterial qualitys due to an antimicrobial agent called bamboo kun found naturally living in the fibres
by using sustainable and reusable materials we are keeping tons and tons of garbage out of landfill. It was estimated in the USA nearly 500 million plastic straws are thrown into landfill every year, thats just the USA and just plastic straws.
Steel straws are great as they are reusable and also last a long period of time. Yet they still have an impact on the earth. You can’t obtain steel without mining the earth which we don’t need to get into the effects of.
Target Market(s)
Environmentally conscious consumers
Products will be sold online and in stores / Heath food stores
Requirements
Must have
- Only earthy colors (if any)
Nice to have
- We would like the packaging to be unique and a little cheeky. Talk about how bamboo straws are the best option.
- Have a “Check me out” or “take a look” arrow looking into the “window” where tot can see the straws.
- “Designed with love in Australia”
- “Australian owned”
- “Percentage of proceeds donated to ......(TBD)

```html
<!DOCTYPE html>
<html lang="en">
<head>
<meta charset="utf-8">
<title>Bamboo Straws – Packaging</title>
<link rel="stylesheet" href="https://fonts.googleapis.com/css2?family=PT+Sans:wght@400;700&family=Roboto:wght@700;900&display=swap">
<style>
  :root{
    --bg:#f1f1f1;
    --kraft:#c8b69b;
    --kraft-side:#bba98d;
    --kraft-tab:#c3b196;
    --olive:#5a6a2c;
    --olive-dark:#48561f;
    --ink:#2e2f1c;
    --black:#1c1c1c;
    --straw:#d9bf8c;
  }
  *{box-sizing:border-box;margin:0;padding:0}
  html,body{width:1200px;height:1200px;overflow:hidden;background:var(--bg)}
  body{position:relative;font-family:"PT Sans",sans-serif;color:var(--ink)}

  .pack{position:absolute;top:140px;width:430px;height:940px}
  .pack--back{left:100px}
  .pack--front{left:670px}

  .hang-tab{position:absolute;left:0;top:0;width:360px;height:80px;background:var(--kraft-tab);border-radius:4px 4px 0 0}
  .hang-hole{position:absolute;left:50%;top:26px;width:96px;height:28px;margin-left:-48px;background:var(--bg);border-radius:14px}

  .panel{position:absolute;top:80px;height:860px}
  .panel-face{left:0;width:360px;background:var(--kraft)}
  .panel-side{left:360px;width:70px;background:var(--kraft-side)}

  .brand{position:absolute;left:50%;border-radius:50%;background:var(--olive);display:flex;align-items:center;justify-content:center;color:var(--kraft);font-family:"PT Sans",sans-serif;font-weight:400;z-index:2}
  .brand--back{top:10px;width:112px;height:112px;margin-left:-56px;font-size:21px}
  .brand--front{top:40px;width:156px;height:156px;margin-left:-78px;font-size:29px}

  .story-frame{position:absolute;left:20px;right:20px;top:68px;bottom:22px;border:2px solid var(--olive);border-radius:16px;padding:64px 16px 10px;text-align:center;font-size:11.4px;line-height:1.42}
  .story-frame p{margin-bottom:9px}
  .story-frame .lead{font-weight:700}

  .side-copy{position:absolute;left:12px;top:150px;width:46px;height:360px;writing-mode:vertical-rl;color:var(--olive);font-size:13px;line-height:1.4;letter-spacing:.3px}
  .side-copy strong{font-weight:700}
  .side-map{position:absolute;left:18px;top:60px;width:34px;height:62px;border-radius:10px;background:var(--olive-dark)}
  .side-bamboo{position:absolute;left:0;right:0;bottom:0;height:380px;background:linear-gradient(180deg,rgba(90,106,44,0) 0%,rgba(90,106,44,.22) 100%)}

  .title{position:absolute;left:0;right:0;text-align:center;font-family:"Roboto",sans-serif;font-weight:900;line-height:1}
  .title--bamboo{top:240px;font-size:58px;color:var(--olive);letter-spacing:1px}
  .title--straws{top:304px;font-size:44px;color:var(--black)}

  .illustration-bamboo{position:absolute;left:0;right:0;bottom:0;height:380px;background:linear-gradient(180deg,rgba(90,106,44,0) 0%,rgba(90,106,44,.25) 100%)}

  .window{position:absolute;left:60px;top:420px;width:250px;height:250px;border-radius:50%;border:5px solid var(--olive);background:linear-gradient(90deg,#c9a872 0%,var(--straw) 30%,#c49d63 55%,var(--straw) 80%,#b89257 100%);z-index:2}
  .window-tail{position:absolute;left:190px;top:640px;z-index:1}

  .callout{position:absolute;left:18px;top:380px;width:92px;height:92px;border-radius:50%;background:var(--olive);color:var(--kraft);font-weight:700;font-size:19px;line-height:1.05;display:flex;align-items:center;justify-content:center;text-align:center;transform:rotate(-14deg);z-index:3}
  .callout-arrow{position:absolute;left:82px;top:448px;z-index:3}

  .donate{position:absolute;left:26px;bottom:40px;width:118px;height:118px;border-radius:50%;background:var(--olive);color:var(--kraft);text-align:center;padding-top:18px;z-index:2}
  .donate-figure{font-family:"Roboto",sans-serif;font-weight:900;font-size:40px;line-height:1}
  .donate-label{font-size:15px;font-weight:700;margin-top:4px}
  .donate-blank{font-size:13px;letter-spacing:1px}
</style>
</head>
<body>

<section class="pack pack--back" aria-label="Back of pack">
  <div class="hang-tab"><span class="hang-hole"></span></div>
  <div class="panel panel-face">
    <div class="brand brand--back">greenstem</div>
    <div class="story-frame">
      <p class="lead">Bamboo is one most sustainable plants in the world! It can grow up to 1m in just 24 hours. Bamboo is naturally anti-bacterial, anti fungal and odour resistant fibre. To grow Bamboo does not require fertiliser or any other harmful pesticides</p>
      <p>Bamboo is a viable replacement for wood. A Large tree can take over 35 years to mature, bamboo can take just 3, a single clump of bamboo can produce up to 15 kilometres of usable pole in its lifetime. It can out yield pine wood 6 to 1 in biomass production. It is the only plant left in the race to matching human consumption and deforestation one of its greatest qualities is after harvest its ability to renew growth is second to none</p>
      <p class="lead">Bamboo straws are reusable and with care can last up to a year. They have anti bacterial qualitys due to an antimicrobial agent called bamboo kun found naturally living in the fibres by using sustainable and reusable materials we are keeping tons and tons of garbage out of landfill. It was estimated in the USA nearly 500 million plastic straws are thrown into landfill every year, thats just the USA and just plastic straws.</p>
      <p>Steel straws are great as they are reusable and also last a long period of time. Yet they still have an impact on the earth. You can't obtain steel without mining the earth which we don't need to get into the effects of.</p>
    </div>
  </div>
  <div class="panel panel-side">
    <div class="side-map" role="img" aria-label="Map of Australia"></div>
    <p class="side-copy">Designed with <strong>LOVE</strong> in Australia<br><strong>Australian owned</strong></p>
    <div class="side-bamboo" role="img" aria-label="Line drawing of bamboo stalks and leaves"></div>
  </div>
</section>

<section class="pack pack--front" aria-label="Front of pack">
  <div class="hang-tab"><span class="hang-hole"></span></div>
  <div class="panel panel-face">
    <div class="brand brand--front">greenstem</div>
    <h1 class="title title--bamboo">BAMBOO</h1>
    <h2 class="title title--straws">STRAWS</h2>
    <div class="illustration-bamboo" role="img" aria-label="Line drawing of bamboo stalks and leaves"></div>
    <svg class="window-tail" width="70" height="70" viewBox="0 0 70 70" aria-hidden="true"><path d="M0 0 L70 0 L60 62 Z" fill="var(--olive)"/></svg>
    <div class="window" role="img" aria-label="Window showing four bamboo straws and a cleaning brush"></div>
    <div class="callout">Check<br>me out</div>
    <svg class="callout-arrow" width="40" height="36" viewBox="0 0 40 36" aria-hidden="true"><path d="M0 0 L40 8 L12 36 Z" fill="var(--olive)"/></svg>
    <div class="donate">
      <div class="donate-figure">5%</div>
      <div class="donate-label">Donated to</div>
      <div class="donate-blank">........</div>
    </div>
  </div>
  <div class="panel panel-side">
    <p class="side-copy" style="top:40px">Designed with <strong>LOVE</strong> in Australia<br><strong>Australian owned</strong></p>
    <div class="side-map" style="top:420px" role="img" aria-label="Map of Australia"></div>
    <div class="side-bamboo" role="img" aria-label="Line drawing of bamboo stalks and leaves"></div>
  </div>
</section>

</body>
</html>
```